Velmora Power

We need a business card for "Velmora power". I have uploaded the logo, the color of the card should be according to the logo "Blackish".
Basically velmora power is a solar company.
Also we would like a sample file in which we can edit the information such names and contact details ourselves
The card would be two sided with following details
1- logo on front and underneath the logo there should be a line saying
"Brighter . Smarter . Power"
2-website i.e "www.velmorapower.example"
3- Icons for Facebook and Instagram that tells the clients we are available on both social sites.
4- name of the person with his/her designation underneath and email address
5-contact number
6- 1-800--- number with the extension number

its up to the designer how he/she places the details,but it must look professional

5-contact number

Requirements
Must have
• 1- logo on front and underneath the logo there should be a line saying
• "Brighter . Smarter . Power"
• 2-website i.e "www.velmorapower.example"
• 3- Icons for Facebook and Instagram that tells the clients we are available on both social sites.
• 4- name of the person with his/her designation underneath and email address
• 5-contact number of the person
• 6- 1-800--- number with the extension number
• 7-card should be in black shade like the logo

```html
<!DOCTYPE html>
<html lang="en">
<head>
<meta charset="utf-8">
<title>Velmora Power – Business Card</title>
<link rel="stylesheet" href="https://fonts.googleapis.com/css2?family=Roboto:wght@400;500&family=Roboto+Condensed:wght@500;700&family=Poppins:wght@700&display=swap">
<style>
  :root {
    --stage: #ece9e4;
    --card-dark: #1f2022;
    --brand-green: #8dc63f;
    --ink-white: #f2f2f2;
    --ink-grey: #a9abad;
    --rule-grey: #6d6f72;
    --ink-black: #111111;
  }
  * { margin: 0; padding: 0; box-sizing: border-box; }
  html, body { width: 1200px; height: 960px; overflow: hidden; }
  body { background: var(--stage); position: relative; font-family: "Roboto", Arial, sans-serif; }

  .card { position: absolute; width: 600px; height: 342px; border-radius: 20px; overflow: hidden; box-shadow: 0 3px 8px rgba(0,0,0,.25); }

  /* Front */
  .card--front { left: 314px; top: 113px; background: var(--card-dark); }
  .card--front .accent-band { position: absolute; left: 0; right: 0; bottom: 0; height: 17px; background: var(--brand-green); border-top: 3px solid var(--rule-grey); }
  .brand-lockup { position: absolute; right: 44px; top: 46px; text-align: right; }
  .brand-lockup .brand-name { font-family: "Roboto Condensed", Arial, sans-serif; font-weight: 700; font-size: 30px; color: var(--brand-green); line-height: 1; }
  .brand-lockup .tagline { margin-top: 10px; font-size: 12.5px; color: var(--ink-grey); letter-spacing: .2px; }

  .person { position: absolute; left: 30px; top: 168px; }
  .person .name { font-family: "Roboto Condensed", Arial, sans-serif; font-weight: 500; font-size: 23px; color: var(--brand-green); line-height: 1; }
  .person .role { margin-top: 6px; font-size: 15px; font-weight: 500; color: var(--ink-white); }

  .divider { position: absolute; left: 30px; right: 43px; top: 221px; height: 1px; background: var(--rule-grey); }

  .contacts { position: absolute; left: 30px; top: 234px; list-style: none; }
  .contacts li { display: flex; align-items: center; height: 19.5px; font-size: 14.5px; color: var(--ink-white); }
  .contacts svg { width: 13px; height: 13px; margin-right: 10px; fill: var(--brand-green); }

  .social { position: absolute; right: 43px; top: 270px; display: flex; gap: 6px; }
  .social .social-badge { width: 17px; height: 17px; background: var(--brand-green); border-radius: 2px; }

  /* Back */
  .card--back { left: 311px; top: 472px; background: var(--brand-green); }
  .back-lockup { position: absolute; left: 0; right: 0; top: 132px; text-align: center; }
  .back-lockup .brand-name { font-family: "Poppins", Arial, sans-serif; font-weight: 700; font-size: 40px; color: var(--ink-black); line-height: 1.1; }
  .back-lockup .website { margin-top: 24px; font-size: 13.5px; font-weight: 500; letter-spacing: 2.6px; color: var(--ink-black); }
</style>
</head>
<body>

<section class="card card--front" aria-label="Business card front">
  <div class="brand-lockup">
    <div class="brand-name">Velmora Power</div>
    <div class="tagline">Brighter . Smarter . Power</div>
  </div>

  <div class="person">
    <div class="name">DANIEL REYES</div>
    <div class="role">CEO/FOUNDER</div>
  </div>

  <div class="divider"></div>

  <ul class="contacts">
    <li>
      <svg viewBox="0 0 16 16" aria-hidden="true"><path d="M4 0h8a1.5 1.5 0 0 1 1.5 1.5v13A1.5 1.5 0 0 1 12 16H4a1.5 1.5 0 0 1-1.5-1.5v-13A1.5 1.5 0 0 1 4 0zm0 2v10.5h8V2zm4 11.3a.9.9 0 1 0 0 1.8.9.9 0 0 0 0-1.8z"/></svg>
      1-800-555-0142
    </li>
    <li>
      <svg viewBox="0 0 16 16" aria-hidden="true"><path d="M1 3h14v1.2L8 8.6 1 4.2zM1 5.6l7 4.4 7-4.4V13H1z"/></svg>
      daniel@velmorapower.example
    </li>
    <li>
      <svg viewBox="0 0 16 16" aria-hidden="true"><path d="M8 0a8 8 0 1 0 0 16A8 8 0 0 0 8 0zm0 1.6a6.4 6.4 0 0 1 5.9 3.9H11c-.6-.4-1.4-.3-1.8.3l-.6 1 1.4 1.4v1.6l1.6 1.6v1.4A6.4 6.4 0 0 1 4 13V11l1.4-1.4V8L3.9 6.6 2.3 7.2A6.4 6.4 0 0 1 8 1.6z"/></svg>
      www.velmorapower.example
    </li>
  </ul>

  <div class="social" aria-label="Social channels">
    <span class="social-badge"></span>
    <span class="social-badge"></span>
  </div>

  <div class="accent-band"></div>
</section>

<section class="card card--back" aria-label="Business card back">
  <div class="back-lockup">
    <div class="brand-name">Velmora Power</div>
    <div class="website">www.velmorapower.example</div>
  </div>
</section>

</body>
</html>
```